Business Card Design

I'm looking for a cool business card design that showcases what my company does... I am the owner and Brava is a play on my last name. The Brava Group is a privately held entity that specializes in media (Brava Media) and financial services (Brava Trading).

Brava Media focuses on the distribution and management of quality entertainment properties to all areas of the media world including broadcast, cable, digital, mobile and social media. Brava Media helps media and entertainment companies create and market great content and ensure that it reaches the widest audience possible.

Brava Media currently represents Ripple TV (www.rippletv-example.com), the fastest growing over the air broadcast network that focuses on programming that appeals to the African American audience. Brava Media also represents two new over the air broadcast networks launching in Summer 2014 - Harbor TV (www.harbortv-example.com) and Maple TV (www.mapletv-example.com).

Brava Media is an investor and business partner in SunDrift (www.sundrift-example.com) - a mobile social platform that empowers the user to choose how long your photos and videos live online.

Brava Media also represents KRN Enterprises (www.krnent-example.com), an independent producer that creates talent-driven and cost-effective programming around emerging talent and Clearbrook Content, a prolific producer of multimedia content including QXN's hit program - Velvet Hall.

Brava Trading manages a family office and focuses on building meaningful partnerships with all major financial institutions with a heavy concentration on IPO and secondary offerings.

Industry/Entity Type

Entertainment

Contact Information for Business Card

Martin Hale
12 Cobalt Lane
Roslyn New York 11492
O 516.555.0143
C 516.555.0178

```html
<!DOCTYPE html>
<html lang="en">
<head>
<meta charset="utf-8">
<title>The Brava Group – Business Card</title>
<link rel="stylesheet" href="https://fonts.googleapis.com/css2?family=Lato:wght@400;700;900&display=swap">
<style>
  :root {
    --canvas: #e9e8e6;
    --card-dark: #6e675f;
    --card-light: #ffffff;
    --orange: #e07b24;
    --stone: #6b6560;
    --cream: #f2eccb;
    --ink: #5d5852;
  }
  * { box-sizing: border-box; margin: 0; padding: 0; }
  html, body {
    width: 1200px; height: 900px; overflow: hidden;
    background: var(--canvas);
    font-family: "Lato", sans-serif;
  }
  .canvas {
    position: relative; width: 1200px; height: 900px;
    display: flex; flex-direction: column; align-items: center; justify-content: center; gap: 40px;
  }
  .card {
    position: relative; width: 700px; height: 400px;
    box-shadow: 0 6px 18px rgba(0,0,0,0.15);
  }
  .card--front { background: var(--card-dark); }
  .card--back { background: var(--card-light); }

  /* Brand lockup: name beside a plain circle */
  .brand { position: absolute; display: flex; align-items: center; }
  .brand__disc { border-radius: 50%; flex: none; }
  .brand__name {
    font-weight: 900; text-transform: uppercase; line-height: 1.02; letter-spacing: 0.01em;
  }
  .card--front .brand { left: 120px; top: 110px; gap: 28px; }
  .card--front .brand__disc { width: 170px; height: 170px; background: var(--cream); }
  .card--front .brand__name { color: var(--cream); font-size: 62px; }

  .card--back .brand { left: 40px; top: 140px; gap: 18px; }
  .card--back .brand__disc { width: 96px; height: 96px; background: #f1ebcd; }
  .card--back .brand__name { color: var(--orange); font-size: 34px; }

  .contact { position: absolute; left: 405px; top: 78px; }
  .contact__name {
    color: var(--orange); font-weight: 700; font-size: 24px; letter-spacing: 0.08em;
  }
  .contact__title {
    color: var(--ink); font-weight: 700; font-size: 17px; letter-spacing: 0.08em; margin-top: 2px;
  }
  .contact__lines { list-style: none; margin-top: 34px; }
  .contact__line {
    display: flex; align-items: center; gap: 14px;
    color: var(--ink); font-size: 19px; letter-spacing: 0.05em; margin-bottom: 9px;
  }
  .contact__line svg { width: 18px; height: 18px; flex: none; fill: var(--orange); }
  .contact__address {
    margin-top: 26px; color: var(--orange); font-weight: 700; font-size: 21px; line-height: 1.15;
  }
</style>
</head>
<body>
<main class="canvas">
  <section class="card card--front" aria-label="Card front">
    <div class="brand">
      <span class="brand__disc"></span>
      <span class="brand__name">The Brava<br>Group</span>
    </div>
  </section>

  <section class="card card--back" aria-label="Card back">
    <div class="brand">
      <span class="brand__disc"></span>
      <span class="brand__name">The Brava<br>Group</span>
    </div>

    <div class="contact">
      <p class="contact__name">MARTIN HALE</p>
      <p class="contact__title">PRINCIPAL</p>
      <ul class="contact__lines">
        <li class="contact__line">
          <svg viewBox="0 0 24 24" aria-hidden="true"><path d="M6.6 10.8a15.5 15.5 0 0 0 6.6 6.6l2.2-2.2a1 1 0 0 1 1-.25 11.4 11.4 0 0 0 3.6.57 1 1 0 0 1 1 1V20a1 1 0 0 1-1 1A17 17 0 0 1 3 4a1 1 0 0 1 1-1h3.5a1 1 0 0 1 1 1c0 1.25.2 2.45.57 3.6a1 1 0 0 1-.25 1z"/></svg>
          <span>516.555.0143</span>
        </li>
        <li class="contact__line">
          <svg viewBox="0 0 24 24" aria-hidden="true"><path d="M7 1h10a2 2 0 0 1 2 2v18a2 2 0 0 1-2 2H7a2 2 0 0 1-2-2V3a2 2 0 0 1 2-2zm0 4v11h10V5zm5 13.2a1.3 1.3 0 1 0 0 2.6 1.3 1.3 0 0 0 0-2.6z"/></svg>
          <span>516.555.0178</span>
        </li>
        <li class="contact__line">
          <svg viewBox="0 0 24 24" aria-hidden="true"><path d="M2 5h20v14H2zm2 2v.4l8 5.2 8-5.2V7zm0 2.8V17h16V9.8l-8 5.2z"/></svg>
          <span>mhale@thebravagroup-example.com</span>
        </li>
      </ul>
      <p class="contact__address">12 Cobalt Lane Roslyn<br>New York 11492</p>
    </div>
  </section>
</main>
</body>
</html>
```